Professional website for psychological services

Create a professional, easy to navigate website using soothing coastal images and incorporate company logo in design. Website is for a small private clinic that provides psychological services and must be appealing to professional men and women. A website I really like is www.velmorlodge.example I would love something like similar.

Target Market(s)

Professional men and women seeking psychological services

Industry/Entity Type

Mental Health

Number of Pages Required

5+ page

Requirements
Must have
• The website must incorporate the logo provided. The name of the company/website is Brindle Oak Wellness Aftercare. Colors must compliment the logo, must be coastal and soothing yet very professional. I would like a website like www.velmorlodge.example
• Pages will be:Home, Services, FAQ and Contact Us. The images included of the building and office are for the contact us page. Under the tab Servies: Individual Psychotherapy, Family Therapy, EMDR I will provide specific content for each.
Nice to have
• I want the website to be easy to navigate and the font easy to read. The writing on the logo is very light and I'm open to changing it slightly if it will be better aesthetically.
Should not have
• Please no pictures of any swimsuits, alcoholic beverages, etc. This is a professional psychological clinic.

```html
<!DOCTYPE html>
<html lang="en">
<head>
<meta charset="utf-8">
<title>Brindle Oak Wellness Aftercare</title>
<link rel="stylesheet" href="https://fonts.googleapis.com/css2?family=Crimson+Text:wght@400;600&family=Raleway:wght@500;600;700&family=Lato:wght@400;700&display=swap">
<style>
:root{
  --teal:#1fb9d6;
  --teal-dark:#17a3bd;
  --ink:#1e1e1e;
  --text:#555;
  --muted:#888;
  --line:#dcdcdc;
  --paper:#fff;
  --mist:#efefef;
  --footer:#262626;
  --footer-text:#9a9a9a;
}
*{box-sizing:border-box;margin:0;padding:0}
html,body{width:1200px;height:3529px;overflow:hidden}
body{position:relative;background:var(--paper);font-family:"Lato",sans-serif;color:var(--text)}
.abs{position:absolute}

/* header */
.site-header{left:0;top:0;width:1200px;height:216px;background:var(--paper)}
.brand{left:118px;top:50px;display:flex;flex-direction:column;align-items:center;width:230px}
.brand-dot{width:30px;height:30px;border-radius:50%;background:var(--teal);margin-bottom:10px}
.brand-name{font-family:"Crimson Text",serif;font-size:46px;color:var(--teal);line-height:1}
.brand-tag{font-family:"Lato",sans-serif;font-size:8px;letter-spacing:2px;color:var(--teal);margin-top:8px}
.main-nav{left:673px;top:124px;display:flex;font-family:"Crimson Text",serif;font-size:22px;color:var(--ink);letter-spacing:.5px}
.main-nav span{padding:0 12px;border-left:1px solid var(--ink);line-height:24px}
.main-nav span:first-child{border-left:0;padding-left:0}

/* hero */
.hero{left:0;top:216px;width:1200px;height:568px;background:linear-gradient(180deg,#ebe6de 0%,#f1ede7 55%,#b9ab95 78%,#6f5e45 100%)}
.hero-photo{left:0;top:0;width:560px;height:568px;background:linear-gradient(90deg,#a0704a 0%,#c9a07c 50%,rgba(220,200,178,0) 100%)}
.hero-copy{left:600px;top:160px;width:520px;text-align:right}
.hero-title{font-family:"Raleway",sans-serif;font-weight:600;font-size:52px;line-height:56px;color:var(--teal)}
.hero-sub{font-family:"Raleway",sans-serif;font-weight:700;font-size:18px;color:var(--ink);margin-top:4px;letter-spacing:.3px}
.hero-btn{left:748px;top:553px;width:219px;height:35px;background:var(--teal);color:#fff;font-family:"Raleway",sans-serif;font-weight:700;font-size:17px;display:flex;align-items:center;justify-content:center}

/* welcome */
.welcome-title{left:148px;top:845px;font-family:"Crimson Text",serif;font-size:54px;color:var(--ink)}
.welcome-body{left:148px;top:930px;width:448px;font-size:15px;line-height:21px;color:var(--text)}
.welcome-body p{margin-bottom:21px}
.signature{left:148px;top:1205px;display:flex;align-items:center;font-family:"Crimson Text",serif;font-size:19px;color:var(--ink);letter-spacing:.5px}
.signature i{display:block;width:130px;height:1px;background:var(--line);margin-left:20px}
.portrait{left:666px;top:854px;width:381px;height:372px;background:linear-gradient(160deg,#3f7a2e 0%,#6f9b4c 40%,#3b2a20 70%,#20242c 100%)}

/* services */
.services{left:0;top:1308px;width:1200px;height:772px;background:var(--teal)}
.services-title{left:0;top:75px;width:1200px;text-align:center;font-family:"Crimson Text",serif;font-size:50px;color:#fff}
.services-intro{left:260px;top:156px;width:680px;text-align:center;font-size:15px;line-height:21px;color:#fff}
.service-card{top:257px;width:287px;height:421px;background:#fff}
.service-img{width:100%;height:219px}
.service-name{font-family:"Raleway",sans-serif;font-weight:600;font-size:23px;line-height:28px;color:var(--teal);text-align:center;margin:20px 20px 0;height:62px;display:flex;align-items:center;justify-content:center}
.service-text{font-size:14px;line-height:20px;color:var(--text);text-align:center;padding:12px 30px 0}
.more{left:50%;bottom:-18px;margin-left:-18px;width:36px;height:36px}

/* faq */
.faq-title{left:0;top:2155px;width:1200px;text-align:center;font-family:"Crimson Text",serif;font-size:52px;color:var(--ink)}
.faq-item{width:470px;height:61px;background:#fff;box-shadow:0 2px 6px rgba(0,0,0,.18);display:flex;align-items:center;padding-left:28px;font-size:15px;color:#333}
.faq-item svg{margin-right:20px;flex:none}

/* contact */
.contact-photo{left:0;top:2699px;width:572px;height:492px;background:linear-gradient(180deg,#e8ecef 0%,#9aa98a 35%,#a87f62 58%,#4f7a3a 80%,#6a5f55 100%)}
.contact-panel{left:572px;top:2699px;width:628px;height:492px;background:var(--mist)}
.contact-title{left:654px;top:2770px;font-family:"Crimson Text",serif;font-size:52px;color:var(--ink)}
.field{background:#fff;border:1px solid #e2e2e2;font-size:14px;color:#777;padding:0 12px;display:flex;align-items:center}
.field.area{align-items:flex-start;padding-top:8px}
.submit{left:654px;top:3064px;width:132px;height:33px;border-radius:17px;background:var(--teal);color:#fff;font-weight:700;font-size:14px;display:flex;align-items:center;justify-content:center}

/* footer */
.site-footer{left:0;top:3191px;width:1200px;height:338px;background:var(--footer)}
.foot-brand{left:150px;top:70px;width:160px;display:flex;flex-direction:column;align-items:center}
.foot-brand .brand-dot{width:20px;height:20px;margin-bottom:8px}
.foot-brand .brand-name{font-size:34px}
.foot-phone{left:148px;top:190px;width:170px;text-align:center;font-family:"Raleway",sans-serif;font-weight:700;font-size:20px;color:var(--teal)}
.foot-col{top:70px}
.foot-col h3{font-family:"Raleway",sans-serif;font-weight:700;font-size:19px;color:#fff;margin-bottom:18px}
.foot-col li{list-style:none;font-size:13px;line-height:26px;color:var(--footer-text)}
.post{margin-bottom:16px}
.post b{display:block;font-size:13px;color:#fff;font-weight:700}
.post small{font-size:10px;color:var(--teal)}
.hours{font-size:13px;line-height:20px;color:var(--footer-text)}
.socials{display:flex;gap:9px;margin-top:22px}
.socials span{width:22px;height:22px;background:#4a4a4a;display:block}
.copyright{left:153px;top:3468px;font-size:11px;color:var(--footer-text)}
</style>
</head>
<body>

<header class="site-header abs">
  <div class="brand abs">
    <span class="brand-dot"></span>
    <span class="brand-name">Brindle Oak</span>
    <span class="brand-tag">WELLNESS AFTERCARE</span>
  </div>
  <nav class="main-nav abs"><span>HOME</span><span>SERVICES</span><span>FAQ</span><span>CONTACT US</span></nav>
</header>

<section class="hero abs">
  <div class="hero-photo abs" role="img" aria-label="Smiling woman with wind-blown hair on a hazy coastal shore"></div>
  <div class="hero-copy abs">
    <h1 class="hero-title">Brindle Oak Wellness Aftercare.</h1>
    <p class="hero-sub">INDIVIDUAL PSYCHOTHERAPY &nbsp;I FAMILY THERAPY &nbsp;I &nbsp;EMDR</p>
  </div>
</section>
<div class="hero-btn abs">MAKE APPOINTMENT</div>

<h2 class="welcome-title abs">Welcome!</h2>
<div class="welcome-body abs">
  <p>Lorem ipsum dolor sit amet, consectetur adipiscing elit. Quid autem habent admirationis, cum prope accesseris? An hoc usque quaque, aliter in vita? Non igitur de improbo, sed de callido improbo quaerimus, qualis Q.</p>
  <p>Nam quibus rebus efficiuntur voluptates, eae non sunt in potestate sapientis. Negare non possum. Huic mori optimum esse propter desperationem sapientiae, illi propter spem vivere.</p>
  <p>Quid enim me prohiberet Epicureum esse, si probarem, quae ille diceret? Qui-vere falsone, quaerere mittimus-dicitur oculis se privasse;</p>
</div>
<div class="signature abs">MARISOL VENN<i></i></div>
<div class="portrait abs" role="img" aria-label="Portrait of the clinic's therapist in front of green foliage"></div>

<section class="services abs">
  <h2 class="services-title abs">Psychotherapy Services</h2>
  <p class="services-intro abs">Lorem ipsum dolor sit amet, consectetur adipiscing elit. Quid autem habent admirationis, cum prope accesseris? An hoc usque quaque, aliter in vita.</p>

  <article class="service-card abs" style="left:144px">
    <div class="service-img" role="img" aria-label="Young man talking with a therapist" style="background:linear-gradient(135deg,#d9d9d9,#9b948c 60%,#5d5a58)"></div>
    <h3 class="service-name">Individual Psychotherapy</h3>
    <p class="service-text">Lorem ipsum dolor sit amet, consectetur adipiscing elit. Quid autem habent admirationis.</p>
    <svg class="more abs" viewBox="0 0 36 36"><circle cx="18" cy="18" r="16" fill="#fff" stroke="var(--teal)" stroke-width="2"/><path d="M18 11v14M11 18h14" stroke="var(--teal)" stroke-width="2"/></svg>
  </article>

  <article class="service-card abs" style="left:456px">
    <div class="service-img" role="img" aria-label="Parents and young child sitting together at home" style="background:linear-gradient(135deg,#e9d9c6,#b58d6e 55%,#6a5a4d)"></div>
    <h3 class="service-name">Family Therapy</h3>
    <p class="service-text">An hoc usque quaque, aliter in vita? Non igitur de improbo, sed de callido improbo quaerimus, qualis Q. Nam quibus rebus efficiuntur</p>
    <svg class="more abs" viewBox="0 0 36 36"><circle cx="18" cy="18" r="16" fill="#fff" stroke="var(--teal)" stroke-width="2"/><path d="M18 11v14M11 18h14" stroke="var(--teal)" stroke-width="2"/></svg>
  </article>

  <article class="service-card abs" style="left:769px">
    <div class="service-img" role="img" aria-label="Close-up of an eye with a colourful iris" style="background:linear-gradient(135deg,#f2f2f2,#9a9a9a 55%,#4d7a6a 80%,#c05a8a)"></div>
    <h3 class="service-name">EMDR</h3>
    <p class="service-text">Negare non possum. Huic mori optimum esse propter desperationem sapientiae, illi propter spem vivere. Quid enim me prohiberet</p>
    <svg class="more abs" viewBox="0 0 36 36"><circle cx="18" cy="18" r="16" fill="#fff" stroke="var(--teal)" stroke-width="2"/><path d="M18 11v14M11 18h14" stroke="var(--teal)" stroke-width="2"/></svg>
  </article>
</section>

<h2 class="faq-title abs">Frequent Ask Questions</h2>
<div class="faq-item abs" style="left:118px;top:2296px"><svg width="14" height="14" viewBox="0 0 14 14"><rect x=".5" y=".5" width="13" height="13" fill="none" stroke="#333"/><path d="M7 4v6M4 7h6" stroke="#333"/></svg>How do I know when it is time to get support?</div>
<div class="faq-item abs" style="left:609px;top:2296px"><svg width="14" height="14" viewBox="0 0 14 14"><rect x=".5" y=".5" width="13" height="13" fill="none" stroke="#333"/><path d="M7 4v6M4 7h6" stroke="#333"/></svg>How do I know when it is time to get support?</div>
<div class="faq-item abs" style="left:118px;top:2374px"><svg width="14" height="14" viewBox="0 0 14 14"><rect x=".5" y=".5" width="13" height="13" fill="none" stroke="#333"/><path d="M7 4v6M4 7h6" stroke="#333"/></svg>What is a Marriage and Family Therapist?</div>
<div class="faq-item abs" style="left:609px;top:2374px"><svg width="14" height="14" viewBox="0 0 14 14"><rect x=".5" y=".5" width="13" height="13" fill="none" stroke="#333"/><path d="M7 4v6M4 7h6" stroke="#333"/></svg>What is a Marriage and Family Therapist?</div>
<div class="faq-item abs" style="left:118px;top:2453px"><svg width="14" height="14" viewBox="0 0 14 14"><rect x=".5" y=".5" width="13" height="13" fill="none" stroke="#333"/><path d="M7 4v6M4 7h6" stroke="#333"/></svg>How long does therapy last?</div>
<div class="faq-item abs" style="left:609px;top:2453px"><svg width="14" height="14" viewBox="0 0 14 14"><rect x=".5" y=".5" width="13" height="13" fill="none" stroke="#333"/><path d="M7 4v6M4 7h6" stroke="#333"/></svg>How long does therapy last?</div>
<div class="faq-item abs" style="left:118px;top:2531px"><svg width="14" height="14" viewBox="0 0 14 14"><rect x=".5" y=".5" width="13" height="13" fill="none" stroke="#333"/><path d="M7 4v6M4 7h6" stroke="#333"/></svg>What type of therapy is offered?</div>
<div class="faq-item abs" style="left:609px;top:2531px"><svg width="14" height="14" viewBox="0 0 14 14"><rect x=".5" y=".5" width="13" height="13" fill="none" stroke="#333"/><path d="M7 4v6M4 7h6" stroke="#333"/></svg>What type of therapy is offered?</div>

<div class="contact-photo abs" role="img" aria-label="Clinic building with palm trees and a fountain"></div>
<div class="contact-panel abs"></div>
<h2 class="contact-title abs">Contact Us</h2>
<div class="field abs" style="left:654px;top:2866px;width:205px;height:38px">Name</div>
<div class="field abs" style="left:880px;top:2866px;width:202px;height:38px">Email</div>
<div class="field abs" style="left:654px;top:2911px;width:205px;height:36px">Phone</div>
<div class="field abs" style="left:880px;top:2911px;width:202px;height:36px">I want to discuss</div>
<div class="field area abs" style="left:654px;top:2958px;width:428px;height:82px">Special Request</div>
<div class="submit abs">Submit Now</div>

<footer class="site-footer abs">
  <div class="foot-brand abs">
    <span class="brand-dot"></span>
    <span class="brand-name">Brindle Oak</span>
  </div>
  <div class="foot-phone abs">800-555-0142</div>
  <div class="foot-col abs" style="left:407px">
    <h3>Quick Links</h3>
    <ul><li>Home</li><li>Services</li><li>FAQ</li><li>Contact Us</li></ul>
  </div>
  <div class="foot-col abs" style="left:624px">
    <h3>From the Blog</h3>
    <div class="post"><b>Lorem ipsum dolor sit amet</b><small>0 Comments</small></div>
    <div class="post"><b>Lorem ipsum dolor sit amet</b><small>0 Comments</small></div>
  </div>
  <div class="foot-col abs" style="left:889px">
    <h3>Open Hours</h3>
    <p class="hours">Monday-Friday 3pm-9pm<br>Saturday 8 am-4pm<br>Sunday Closed</p>
    <div class="socials"><span></span><span></span><span></span><span></span></div>
  </div>
</footer>
<p class="copyright abs">Brindle Oak © 2016. All Rights Reserved Terms of Use and Privacy Policy</p>

</body>
</html>
```